Maple Cove Laser Dermal Studio needs an 8 page WP redesign

We need a colorful re-design for an 8 page Wordpress website. The current preliminary website is live. The home page URL is http://maplecovelaserdermalstudio.com The new logo is live on the website also. I would like a (re)design using the colors that are represented by the new logo file, and any additional complimentary colors. The information regarding the business can be found on the website already, so please review it for insight. The name of the business is "Maple Cove Laser Dermal Studio".

Target Market(s)

The targeted website viewer is an adult female between the ages of 30 and 75 who is interested in facial renewal, wart removal and scar removal. This website should inspire in the target viewer the benefits of laser facial renewal, wart removal and new scar removal. Potential website viewers are wanting and searching for improved skin health and appearance. The website must represent the essence of a professional spa business.

Industry/Entity Type

Business

Font styles to use
Sans Serif

Requirements
Must have
• - The phone number placed in a visible and high value widget area that allows mobile phone browser dialing.

```html
<!DOCTYPE html>
<html lang="en">
<head>
<meta charset="utf-8">
<title>Maple Cove Laser Dermal Studio</title>
<link href="https://fonts.googleapis.com/css2?family=Play:wght@400;700&family=Open+Sans:wght@400;600&display=swap" rel="stylesheet">
<style>
:root{
  --purple:#9a12a6;
  --purple-dark:#7d0a8a;
  --purple-soft:#c86bd0;
  --pink:#e66bc1;
  --ink:#1d1d1d;
  --grey:#5a5a5a;
  --rule:#d8d8d8;
  --footer:#232323;
  --white:#ffffff;
}
*{box-sizing:border-box;margin:0;padding:0}
html,body{width:962px;height:1200px;overflow:hidden;background:var(--white)}
body{font-family:"Play",sans-serif;color:var(--ink);position:relative}
a{color:inherit;text-decoration:none}
.hero{position:absolute;left:0;top:0;width:962px;height:481px;
  background:linear-gradient(100deg,#f3d9d0 0%,#fbeee8 30%,#f7ece6 55%,#e7f1e6 75%,#d7eef2 100%)}
.hero-photo{position:absolute;inset:0;
  background:radial-gradient(ellipse 260px 200px at 160px 230px,rgba(236,190,175,.7),transparent 70%),
  radial-gradient(ellipse 220px 260px at 770px 250px,rgba(245,210,190,.75),transparent 70%),
  radial-gradient(ellipse 300px 90px at 300px 440px,rgba(250,215,235,.8),transparent 70%)}
.top-phone{position:absolute;right:80px;top:10px;font-size:21px;color:var(--purple);display:flex;align-items:center;gap:8px}
.top-phone svg{width:17px;height:17px}
.navbar{position:absolute;left:0;top:42px;width:962px;height:100px;background:rgba(255,255,255,.55)}
.brand{position:absolute;left:74px;top:30px;width:210px;display:flex;align-items:center;gap:8px;font-family:"Play",sans-serif;font-size:17px;line-height:1.15;color:var(--purple-dark);font-weight:700}
.brand-dot{width:18px;height:18px;border-radius:50%;background:var(--purple);flex:none}
.main-nav{position:absolute;left:313px;top:40px;display:flex;gap:0;font-size:15px}
.main-nav a{margin-right:29px}
.main-nav a.active{color:var(--purple)}
.hero-copy{position:absolute;left:0;width:962px;top:268px;text-align:center}
.hero-title{font-size:32px;font-weight:400;color:#222}
.hero-title span{color:var(--purple)}
.hero-sub{font-size:18px;color:var(--purple);margin-top:4px}
.hero-line{font-size:17.5px;margin-top:8px;color:#2a2a2a}
.col-title{font-size:19px;color:var(--purple);text-align:center;line-height:25px;font-weight:400}
.divider{display:block;margin:5px auto 0}
.services{position:absolute;left:70px;top:490px;width:260px}
.service{position:absolute;left:0;width:256px;height:80px}
.service .thumb{position:absolute;left:0;top:0;width:80px;height:80px;border-radius:50%;border:4px solid var(--purple-soft);z-index:2}
.service .bar{position:absolute;left:50px;top:5px;width:206px;height:67px;
  background:linear-gradient(90deg,#d985d8,var(--purple) 70%);border-radius:2px;
  color:var(--white);font-size:19px;padding-left:52px;line-height:67px}
.t1{background:linear-gradient(135deg,#f5d2be,#e9b59d)}
.t2{background:linear-gradient(135deg,#c79a85,#a7786a)}
.t3{background:linear-gradient(135deg,#efc7b2,#d8a592)}
.about{position:absolute;left:340px;top:490px;width:281px}
.about .vline{position:absolute;top:10px;width:1px;height:335px;background:var(--purple)}
.about .vline::before,.about .vline::after{content:"";position:absolute;left:-4px;width:9px;height:9px;transform:rotate(45deg);background:var(--purple)}
.about .vline::before{top:-4px}
.about .vline::after{bottom:-4px}
.about-text{font-family:"Open Sans",sans-serif;font-size:11.6px;line-height:18.3px;color:var(--grey);text-align:justify;padding:0 10px;margin-top:12px}
.about-text p+p{margin-top:16px}
.read-more{display:block;width:109px;height:33px;margin:9px auto 0;background:var(--purple);color:var(--white);font-size:16.5px;text-align:center;line-height:33px;border-radius:2px}
.contact{position:absolute;left:633px;top:490px;width:254px}
.contact-photo{width:240px;height:150px;margin:8px auto 0;border-bottom:1px solid #f0d6ee;
  background:radial-gradient(ellipse 60px 80px at 50% 55%,#e8cbbd,#f7efec 70%,#fff 100%)}
.contact-list{font-family:"Open Sans",sans-serif;font-size:11.6px;color:var(--grey);margin-top:14px}
.contact-row{display:flex;align-items:flex-start;gap:14px;margin-left:10px}
.contact-row svg{flex:none;width:16px;height:16px;fill:var(--purple)}
.contact-row .addr{line-height:18.3px}
.contact-phone{font-size:19px;color:var(--purple);margin-top:6px;align-items:center}
.contact-mail{margin-top:3px;align-items:center}
.promo{position:absolute;left:0;top:885px;width:962px;height:190px;background:var(--purple)}
.promo::before{content:"";position:absolute;left:0;top:-4px;width:962px;height:4px;
  background:repeating-linear-gradient(135deg,var(--purple) 0 2px,#fff 2px 4px)}
.badge{position:absolute;left:63px;top:6px;width:181px;height:181px;border-radius:50%;border:4px solid var(--white);
  background:linear-gradient(180deg,#fff 0%,#f3dcf1 55%,#c06acb 100%);
  display:flex;align-items:center;justify-content:center;text-align:center;font-size:26px;line-height:37px;color:#111}
.promo-copy{position:absolute;left:270px;top:18px;width:540px;text-align:center;color:var(--white)}
.promo-head{font-size:19px}
.promo-lead{font-size:17px;line-height:18px;margin-top:14px}
.deal{position:absolute;top:110px;text-align:center;font-size:18px;line-height:25px;color:#1b0420}
.deal .price{font-size:20px;color:var(--white)}
.deal.featured .price{font-size:26px;color:#111;font-weight:700}
.footer{position:absolute;left:0;top:1075px;width:962px;height:125px;background:var(--footer);color:var(--white)}
.foot-nav{position:absolute;left:193px;top:21px;display:flex;font-size:15px}
.foot-nav a{margin-right:29px}
.foot-nav a.active{color:var(--pink)}
.copyright{position:absolute;left:63px;top:75px;font-family:Arial,sans-serif;font-size:10px}
.copyright a{font-weight:700;text-decoration:underline}
.social{position:absolute;right:63px;top:55px;display:flex;gap:17px}
.social span{width:41px;height:41px;border-radius:50%;border:2px solid var(--white);background:var(--purple)}
</style>
</head>
<body>

<section class="hero">
  <div class="hero-photo" role="img" aria-label="Photo of a woman relaxing at a spa among pale orchids beside a woman touching her glowing face"></div>

  <div class="navbar">
    <a class="brand" href="http://maplecovelaserdermalstudio.com"><span class="brand-dot"></span>Maple Cove Laser Dermal Studio</a>
    <nav class="main-nav">
      <a class="active" href="#">Home</a><a href="#">About</a><a href="#">Skin Renewal</a><a href="#">Scar Removal</a><a href="#">Your Visit</a><a href="#">Conact</a><a href="#">Blog</a>
    </nav>
  </div>

  <a class="top-phone" href="tel:5550184420">
    <svg viewBox="0 0 24 24"><path fill="#333" d="M6.6 10.8a15 15 0 0 0 6.6 6.6l2.2-2.2a1 1 0 0 1 1-.25 11.4 11.4 0 0 0 3.6.57 1 1 0 0 1 1 1V20a1 1 0 0 1-1 1A17 17 0 0 1 3 4a1 1 0 0 1 1-1h3.5a1 1 0 0 1 1 1c0 1.25.2 2.45.57 3.6a1 1 0 0 1-.25 1z"/></svg>
    555-018-4420
  </a>

  <div class="hero-copy">
    <h1 class="hero-title"><span>Laser</span> Skin Renewal</h1>
    <p class="hero-sub">is Innovative and Unique</p>
    <p class="hero-line">Restore your youthful skin this year!</p>
  </div>
</section>

<section class="services">
  <h2 class="col-title">Our Services</h2>
  <svg class="divider" width="250" height="12" viewBox="0 0 250 12"><line x1="0" y1="6" x2="105" y2="6" stroke="#cfcfcf"/><line x1="145" y1="6" x2="250" y2="6" stroke="#cfcfcf"/><ellipse cx="125" cy="6" rx="14" ry="3.5" fill="none" stroke="#333" stroke-width="1.5"/></svg>
  <div class="service" style="top:52px"><div class="thumb t1" role="img" aria-label="Photo of a smiling woman's face"></div><a class="bar" href="#">Skin Renewal</a></div>
  <div class="service" style="top:169px"><div class="thumb t2" role="img" aria-label="Close-up photo of a scar on skin"></div><a class="bar" href="#">Scar Removal</a></div>
  <div class="service" style="top:285px"><div class="thumb t3" role="img" aria-label="Photo of a bare foot"></div><a class="bar" href="#">Wart Removal</a></div>
</section>

<section class="about">
  <span class="vline" style="left:0"></span>
  <span class="vline" style="left:280px"></span>
  <h2 class="col-title">Have you considered Laser<br>Skin Renewal Therapy?</h2>
  <svg class="divider" width="250" height="12" viewBox="0 0 250 12"><line x1="0" y1="6" x2="105" y2="6" stroke="#cfcfcf"/><line x1="145" y1="6" x2="250" y2="6" stroke="#cfcfcf"/><ellipse cx="125" cy="6" rx="14" ry="3.5" fill="none" stroke="#333" stroke-width="1.5"/></svg>
  <div class="about-text">
    <p>You will truly love laser skin renewal if your skin is showing signs of premature aging or the skin has sustained sun damage. Conditions such as excessive redness due to sun exposure or fine lines will be concerns of the past. In fact, laser skin therapy is a unique and innovative way to enjoy youthful and healthy skin without resorting to painful and inconvenient surgery. Both men and women are receiving benefits from laser skin therapy.</p>
    <p>The literature contains ample scientific evidence to support laser skin renewal. After this therapy, your skin will produce collagen...</p>
  </div>
  <a class="read-more" href="#">Read More</a>
</section>

<section class="contact">
  <h2 class="col-title">Contact With Us</h2>
  <svg class="divider" width="250" height="12" viewBox="0 0 250 12"><line x1="0" y1="6" x2="105" y2="6" stroke="#cfcfcf"/><line x1="145" y1="6" x2="250" y2="6" stroke="#cfcfcf"/><ellipse cx="125" cy="6" rx="14" ry="3.5" fill="none" stroke="#333" stroke-width="1.5"/></svg>
  <div class="contact-photo" role="img" aria-label="Photo of a woman with hands framing her face beside a white feather"></div>
  <div class="contact-list">
    <div class="contact-row">
      <svg viewBox="0 0 24 24"><path d="M12 2a7 7 0 0 0-7 7c0 5.2 7 13 7 13s7-7.8 7-13a7 7 0 0 0-7-7zm0 9.5A2.5 2.5 0 1 1 12 6.5a2.5 2.5 0 0 1 0 5z"/></svg>
      <address class="addr" style="font-style:normal">Maple Cove Laser Dermal Studio<br>Harborview Wellness Plaza<br>2240 Lakeshore Rd, Suite 12<br>Maple Cove, TX 77000</address>
    </div>
    <a class="contact-row contact-phone" href="tel:5550184420">
      <svg viewBox="0 0 24 24"><path d="M6.6 10.8a15 15 0 0 0 6.6 6.6l2.2-2.2a1 1 0 0 1 1-.25 11.4 11.4 0 0 0 3.6.57 1 1 0 0 1 1 1V20a1 1 0 0 1-1 1A17 17 0 0 1 3 4a1 1 0 0 1 1-1h3.5a1 1 0 0 1 1 1c0 1.25.2 2.45.57 3.6a1 1 0 0 1-.25 1z"/></svg>
      (555) 018-4420
    </a>
    <a class="contact-row contact-mail" href="mailto:info@maplecovelaserdermalstudio.com">
      <svg viewBox="0 0 24 24"><path d="M2 5h20v14H2zm2 2v.5l8 5 8-5V7l-8 5z"/></svg>
      info@maplecovelaserdermalstudio.com
    </a>
  </div>
</section>

<section class="promo">
  <div class="badge">New Years<br>Resolution<br>Special!</div>
  <div class="promo-copy">
    <p class="promo-head">Restore your youthful skin this year!</p>
    <p class="promo-lead">Take advantage of our laser skin renewal specials for single or multiple sessions at low pricing.</p>
  </div>
  <div class="deal featured" style="left:280px;width:135px">1 Single<br>Session Deal<br><span class="price">$199</span></div>
  <div class="deal" style="left:478px;width:140px">3 Sessions<br>Package Deal<br><span class="price">$549</span></div>
  <div class="deal" style="left:704px;width:140px">6 Sessions<br>Package Deal<br><span class="price">$899</span></div>
</section>

<footer class="footer">
  <nav class="foot-nav">
    <a class="active" href="#">Home</a><a href="#">About</a><a href="#">Skin Renewal</a><a href="#">Scar Removal</a><a href="#">Your Visit</a><a href="#">Conact</a><a href="#">Blog</a>
  </nav>
  <p class="copyright">© <a href="http://maplecovelaserdermalstudio.com">Maple Cove Laser Dermal Studio</a> - 2014. All Rights Reserved.</p>
  <div class="social">
    <span role="img" aria-label="Social profile link"></span>
    <span role="img" aria-label="Social profile link"></span>
    <span role="img" aria-label="Social profile link"></span>
  </div>
</footer>

</body>
</html>
```